Executive Coach needs elegant business card design

I need a business card design which includes following info: name, email (same as name, @gmail.com), phone. I'd put that on one side. On the other side i'd like some graphic indicating what i do:
- using questions to help people get great results
- encourage people to try different solutions to overcome old problems
- untangling the mental knot that traps people in vicious circles
- question mental models to get people to see a different point of view.

I'd like an elegant design. Bonus points for providing a different twist on things. I've included 2 designs I started with. Feel free to improve or discard them :-)

```html
<!DOCTYPE html>
<html lang="en">
<head>
<meta charset="utf-8">
<title>Executive Coach Business Card</title>
<link rel="stylesheet" href="https://fonts.googleapis.com/css2?family=Fira+Mono:wght@400&display=swap">
<style>
  :root {
    --brand-blue: #0270b9;
    --paper: #ffffff;
    --ink: #333333;
    --edge-shadow: #b5b5b5;
    --card-border: #9a9a9a;
    --divider: rgba(255, 255, 255, 0.7);
  }
  * { margin: 0; padding: 0; box-sizing: border-box; }
  html, body {
    width: 1200px;
    height: 1000px;
    overflow: hidden;
    background: var(--paper);
  }
  body {
    position: relative;
    font-family: "Fira Mono", monospace;
  }
  .card {
    position: absolute;
    left: 226px;
    width: 747px;
    height: 427px;
    box-shadow: 10px 10px 0 var(--edge-shadow);
  }
  .card--front { top: 35px; background: var(--brand-blue); }
  .card--back  { top: 527px; background: var(--paper); border: 1px solid var(--card-border); }

  .brand {
    position: absolute;
    display: flex;
    align-items: center;
    gap: 10px;
    font-size: 15px;
    letter-spacing: 1.5px;
    white-space: nowrap;
  }
  .brand__dot {
    width: 12px;
    height: 12px;
    border-radius: 50%;
    border: 2px solid currentColor;
  }
  .card--front .brand { left: 80px; top: 215px; color: var(--paper); }
  .card--back .brand  { right: 50px; top: 100px; color: var(--brand-blue); font-size: 13px; }

  .divider {
    position: absolute;
    left: 288px;
    top: 182px;
    width: 1px;
    height: 89px;
    background: var(--divider);
  }
  .tagline {
    position: absolute;
    left: 313px;
    top: 195px;
    color: var(--paper);
    font-size: 15.5px;
    line-height: 22px;
    letter-spacing: 1.6px;
    text-transform: uppercase;
  }

  .contact {
    position: absolute;
    left: 59px;
    top: 206px;
    color: var(--brand-blue);
    font-size: 14px;
    line-height: 20.5px;
    list-style: none;
  }
  .services {
    position: absolute;
    left: 59px;
    top: 312px;
    color: var(--ink);
    font-size: 13.5px;
    line-height: 19px;
    list-style: none;
    letter-spacing: 0.3px;
  }
</style>
</head>
<body>
  <section class="card card--front">
    <div class="brand"><span class="brand__dot"></span>DELORME COACHING</div>
    <span class="divider"></span>
    <p class="tagline">Sometimes a different perspective<br>is all you need to find your way out<br>of a difficult maze...</p>
  </section>

  <section class="card card--back">
    <div class="brand"><span class="brand__dot"></span>DELORME COACHING</div>
    <ul class="contact">
      <li>EXECUTIVE COACH</li>
      <li>name: MARTIN DELORME</li>
      <li>email: MARTINDELORME@MAILBOX.COM</li>
      <li>phone: 612 345678</li>
    </ul>
    <ul class="services">
      <li>Use questions to help people get great results.</li>
      <li>Encourage people to try different solutions to overcome old problems.</li>
      <li>Untangle the mental knot that traps people in vicious circles.</li>
      <li>Question mental models to get people to see a different point of view.</li>
    </ul>
  </section>
</body>
</html>
```